Wordpress Design for a Private Label BBQ Brand

For our new brand, we'd need a new Wordpress website. We'd prefer to run the website on Wordpress

We'd like to include the following
- space for description of the brand
- space for product portfolio (not a shop!)
- space for socials
- space for support
- space for contact

```html
<!DOCTYPE html>
<html lang="en">
<head>
<meta charset="utf-8">
<title>Fiamma – Barbeque Grill Tools</title>
<link href="https://fonts.googleapis.com/css2?family=Libre+Caslon+Text:wght@400;700&family=Lexend:wght@300;400;500;600&display=swap" rel="stylesheet">
<style>
:root{
  --ink:#0d0d0d;
  --white:#ffffff;
  --paper:#f2f2f2;
  --red:#c8262b;
  --orange:#e4521c;
  --flame:#f26a1b;
  --muted:#2a2a2a;
  --line:#e05a22;
  --serif:"Libre Caslon Text", Georgia, serif;
  --sans:"Lexend", Arial, sans-serif;
}
*{box-sizing:border-box;margin:0;padding:0}
html,body{width:1200px;height:3119px;overflow:hidden}
body{position:relative;background:var(--paper);font-family:var(--sans);color:var(--ink)}
.block{position:absolute;left:0;width:1200px}

/* header */
.site-header{top:0;height:130px;background:var(--ink);border-bottom:1px solid #333;display:flex;align-items:center;padding:0 99px}
.brand{display:flex;align-items:center;gap:14px;font-family:var(--serif);font-weight:700;font-size:52px;color:var(--white);letter-spacing:1px}
.brand-dot{width:34px;height:34px;border-radius:50%;background:var(--orange)}
.main-nav{margin-left:auto;display:flex;align-items:center;gap:26px;font-size:19px;color:var(--white)}
.main-nav .sep{width:5px;height:5px;border-radius:50%;background:var(--orange)}

/* hero */
.hero{top:130px;height:700px;background:radial-gradient(ellipse at 50% 80%,#7a2a12 0%,#3a1a10 40%,#0f0c0b 80%)}
.hero-title{position:absolute;top:56px;width:100%;text-align:center;font-family:var(--serif);font-weight:700;font-size:84px;color:var(--white)}
.hero-title span{color:var(--flame)}
.hero-sub{position:absolute;top:156px;width:100%;text-align:center;font-size:33px;color:var(--white);font-weight:400}
.btn{display:inline-flex;align-items:center;justify-content:space-between;background:linear-gradient(90deg,var(--red),var(--flame));color:var(--white);font-weight:600;border-radius:30px}
.hero .btn{position:absolute;left:488px;top:222px;width:224px;height:54px;padding:0 20px 0 20px;font-size:21px}
.btn .dot{width:16px;height:16px;border-radius:50%;background:var(--white)}
.arrow{position:absolute;top:209px;width:48px;height:48px;border:2px solid var(--white);border-radius:50%}
.arrow.prev{left:37px}.arrow.next{left:1115px}
.wave{position:absolute;top:680px;left:0}

/* about */
.about{top:830px;height:496px}
.about-photo{position:absolute;left:109px;top:-31px;width:484px;height:484px;border-radius:50%;background:radial-gradient(circle,#6b1a0c 0%,#2a0d08 60%,#111 100%);border:6px solid #1a1a1a}
.about-text{position:absolute;left:632px;top:-4px;width:456px}
.eyebrow{display:flex;align-items:center;gap:14px;font-size:19px}
.eyebrow::after{content:"";width:74px;height:1px;background:var(--red)}
.about h2{font-family:var(--serif);font-weight:700;font-size:45px;line-height:1.02;color:var(--red);margin:14px 0 16px}
.about p{font-size:13.4px;line-height:18.2px;text-align:justify;color:var(--muted);margin-bottom:18px}
.about .btn{width:180px;height:44px;padding:0 16px;font-size:16px;margin-top:4px}

/* products */
.products{top:1326px;height:923px;background:radial-gradient(ellipse at 50% 40%,#262626 0%,#151515 60%,#0c0c0c 100%)}
.products-head{position:absolute;top:100px;left:98px;width:1003px;display:flex;align-items:center;gap:26px}
.products-head::before,.products-head::after{content:"";flex:1;height:1px;background:var(--line)}
.products-head h2{font-family:var(--serif);font-weight:700;font-size:46px;color:var(--white)}
.product-grid{position:absolute;top:191px;left:98px;width:1003px;display:grid;grid-template-columns:repeat(4,1fr);grid-auto-rows:308px;column-gap:27px;row-gap:29px}
.card{position:relative;background:var(--white);border-radius:4px;border-bottom:4px solid var(--orange);overflow:hidden}
.card.wide{grid-column:span 2}
.card::before{content:"";position:absolute;left:0;bottom:0;width:22px;height:22px;background:var(--orange);border-top-right-radius:22px}
.product-img{position:absolute;top:28px;left:24px;right:24px;height:170px;background:linear-gradient(160deg,#e9e9e9,#bdbdbd);border-radius:3px}
.card h3{position:absolute;left:27px;top:230px;font-family:var(--serif);font-weight:400;font-size:22px;color:var(--red)}
.card span{position:absolute;left:27px;top:264px;font-size:13.5px;color:var(--muted)}

/* contact */
.contact{top:2249px;height:518px;background:linear-gradient(100deg,#d7261f 0%,#e0421c 50%,#ea5d1c 100%)}
.contact .eyebrow{position:absolute;left:100px;top:54px;color:var(--white);font-size:18px}
.contact .eyebrow::after{background:var(--white);width:116px}
.contact h2{position:absolute;left:100px;top:90px;font-family:var(--serif);font-weight:700;font-size:44px;color:var(--white)}
.contact-form{position:absolute;left:100px;top:171px;width:558px;display:grid;grid-template-columns:1fr 1fr;gap:10px 9px}
.field{height:41px;background:var(--white);border:1px solid #ddd;font-family:var(--sans);font-size:13px;color:#888;padding:0 12px;display:flex;align-items:center}
.field.message{grid-column:span 2;height:128px;align-items:flex-start;padding-top:14px}
.send{grid-column:span 2;height:42px;background:var(--ink);color:var(--white);font-size:13px;font-weight:600;display:flex;align-items:center;justify-content:center;border-radius:3px}
.grill-photo{position:absolute;left:690px;top:46px;width:412px;height:412px;border-radius:50%;background:radial-gradient(circle,#8a3a1c 0%,#4a1d10 55%,#1b1b1b 80%);border:10px solid #222}

/* footer */
.site-footer{top:2767px;height:285px;background:var(--paper)}
.col{position:absolute;top:56px}
.col h4{font-size:17px;font-weight:600;color:var(--red);margin-bottom:26px}
.quick{left:97px}
.quick li{list-style:none;font-size:15px;line-height:28.5px}
.divider{position:absolute;top:54px;width:1px;height:152px;background:#bbb}
.reach{left:281px}
.reach h4{margin-left:29px}
.reach p{display:flex;gap:12px;font-size:15px;line-height:19px;margin-bottom:24px}
.reach svg{flex:none;margin-top:2px}
.map{position:absolute;left:562px;top:60px;width:224px;height:183px;border:3px solid var(--orange);border-radius:6px;background:linear-gradient(140deg,#e9ecef 0%,#dfe6e0 50%,#cfe3d4 100%)}
.footer-brand{position:absolute;left:878px;top:64px;width:182px;text-align:center}
.footer-brand .mark{width:60px;height:60px;border-radius:50%;background:var(--orange);margin:0 auto 24px}
.footer-brand .name{font-family:var(--serif);font-weight:700;font-size:36px}
.follow{display:flex;align-items:center;justify-content:center;gap:8px;margin-top:8px;font-size:15px}
.follow i{width:22px;height:22px;border-radius:50%;background:var(--orange);display:block}
.follow i:first-of-type{margin-left:8px}
.copy{top:3052px;height:67px;background:var(--ink);color:var(--white);font-size:13px;display:flex;align-items:center;justify-content:center}
</style>
</head>
<body>

<header class="block site-header">
  <div class="brand"><span class="brand-dot"></span>FIAMMA</div>
  <nav class="main-nav">
    <a>Home</a><span class="sep"></span><a>About</a><span class="sep"></span><a>Products</a><span class="sep"></span><a>Support Us</a><span class="sep"></span><a>Contact</a>
  </nav>
</header>

<section class="block hero" role="img" aria-label="Steaks with rosemary and peppercorns on a flaming grill, a fork piercing one steak">
  <h1 class="hero-title">Welcome To <span>Fiamma</span></h1>
  <p class="hero-sub">The Best Barbeque Grill Tools</p>
  <a class="btn">READ MORE <span class="dot"></span></a>
  <span class="arrow prev"><svg width="44" height="44" viewBox="0 0 44 44"><path d="M25 14l-8 8 8 8" fill="none" stroke="#fff" stroke-width="2.5"/></svg></span>
  <span class="arrow next"><svg width="44" height="44" viewBox="0 0 44 44"><path d="M19 14l8 8-8 8" fill="none" stroke="#fff" stroke-width="2.5"/></svg></span>
</section>
<svg class="wave" width="1200" height="200" viewBox="0 0 1200 200">
  <path d="M0,110 C150,20 300,-5 470,8 C300,22 140,90 0,195Z" fill="#e4521c"/>
  <path d="M0,195 C150,60 300,15 480,30 C650,45 780,110 900,100 C1030,90 1120,60 1200,10 L1200,200 L0,200Z" fill="#f2f2f2"/>
  <path d="M480,30 C650,45 780,110 900,100 C1030,90 1120,60 1200,10" fill="none" stroke="#e4521c" stroke-width="5"/>
</svg>

<section class="block about">
  <div class="about-photo" role="img" aria-label="Black ceramic kamado grill against glowing embers"></div>
  <div class="about-text">
    <div class="eyebrow">About Fiamma</div>
    <h2>THE BEST BARBEQUE GRILL TOOLS</h2>
    <p>Lorem Ipsum is simply dummy text of the printing and typesetting industry. Lorem Ipsum has been the industry's standard dummy text ever since the 1500s, when an unknown printer took a galley of type and scrambled it to make a type specimen book. It has survived not only five centuries, but also the leap into electronic typesetting, remaining essentially unchanged. It was popularised in the 1960s with the release of Letraset sheets containing.</p>
    <p>Lorem Ipsum is simply dummy text of the printing and typesetting industry. Lorem Ipsum has been the industry's standard dummy text ever since the 1500s, when an unknown printer took a galley of type and scrambled it to make a type specimen book. It has survived not only five centuries, but also the leap into electronic typesetting, remaining essentially unchanged.</p>
    <a class="btn">READ MORE <span class="dot"></span></a>
  </div>
</section>

<section class="block products" role="region" aria-label="Our products">
  <div class="products-head"><h2>OUR PRODUCTS</h2></div>
  <div class="product-grid">
    <article class="card wide"><div class="product-img" role="img" aria-label="Stainless steel grill spatula"></div><h3>Fiamma-3pc-2</h3><span>Barbeque Grill Tools</span></article>
    <article class="card"><div class="product-img" role="img" aria-label="Small black kamado grill"></div><h3>Fiamma-13inch-1</h3><span>Barbeque Grill Tools</span></article>
    <article class="card"><div class="product-img" role="img" aria-label="Open case with grill tool set"></div><h3>Fiamma-15pcs-1</h3><span>Barbeque Grill Tools</span></article>
    <article class="card"><div class="product-img" role="img" aria-label="Closed aluminium tool case"></div><h3>Fiamma-15pcs-3</h3><span>Barbeque Grill Tools</span></article>
    <article class="card"><div class="product-img" role="img" aria-label="Multi-purpose grill scraper"></div><h3>Fiamma-15pcs-5</h3><span>Barbeque Grill Tools</span></article>
    <article class="card"><div class="product-img" role="img" aria-label="Silicone basting brush"></div><h3>Fiamma-15pcs-6</h3><span>Barbeque Grill Tools</span></article>
    <article class="card"><div class="product-img" role="img" aria-label="Pair of corn holders"></div><h3>Fiamma-15pcs-7</h3><span>Barbeque Grill Tools</span></article>
  </div>
</section>

<section class="block contact">
  <div class="eyebrow">Fiamma</div>
  <h2>CONTACT FORM</h2>
  <form class="contact-form">
    <div class="field">FIRST NAME*</div><div class="field">LAST NAME*</div>
    <div class="field">E-MAIL*</div><div class="field">PHONE*</div>
    <div class="field message">MESSAGE</div>
    <div class="send">SEND NOW</div>
  </form>
  <div class="grill-photo" role="img" aria-label="Round grill from above with skewers, sausages, corn and vegetables"></div>
</section>

<footer class="block site-footer">
  <div class="col quick">
    <h4>QUICK LINKS</h4>
    <ul><li>Home</li><li>About</li><li>Products</li><li>Support Us</li><li>Contact</li></ul>
  </div>
  <span class="divider" style="left:252px"></span>
  <div class="col reach">
    <h4>CONTACT US</h4>
    <p><svg width="17" height="17" viewBox="0 0 16 16"><circle cx="8" cy="8" r="8" fill="#e4521c"/><path d="M8 3.5a3 3 0 0 0-3 3c0 2.2 3 5.5 3 5.5s3-3.3 3-5.5a3 3 0 0 0-3-3z" fill="#fff"/></svg>48 Harbour Lane, Kelston Bay,<br>Westhaven, 5120</p>
    <p><svg width="17" height="17" viewBox="0 0 16 16"><circle cx="8" cy="8" r="8" fill="#e4521c"/><path d="M5 4l2 0 1 2.2-1.2 1a5 5 0 0 0 2 2l1-1.2 2.2 1v2a1 1 0 0 1-1 1A7 7 0 0 1 4 5a1 1 0 0 1 1-1z" fill="#fff"/></svg>+123 (1) 555 014 2290</p>
    <p><svg width="17" height="17" viewBox="0 0 16 16"><circle cx="8" cy="8" r="8" fill="#e4521c"/><rect x="4" y="5" width="8" height="6" fill="#fff"/><path d="M4 5l4 3.5L12 5" fill="none" stroke="#e4521c" stroke-width="1"/></svg>hello@fiammagrill.example</p>
  </div>
  <span class="divider" style="left:531px"></span>
  <div class="map" role="img" aria-label="Street map showing the company location beside a river reserve"></div>
  <span class="divider" style="left:817px"></span>
  <div class="footer-brand">
    <div class="mark"></div>
    <div class="name">FIAMMA</div>
    <div class="follow">Follow Us <i></i><i></i><i></i></div>
  </div>
</footer>

<div class="block copy">© Copyright - 2023 &nbsp;|&nbsp; Fiamma &nbsp;|&nbsp; All Rights Reserved</div>

</body>
</html>
```